Design a wordpress website for IT consulting firm

We are a fintech+blockchain+full stack + software development consulting team. We offer services in these areas, we would like to design a new wordpress website.

The winner would need to first come with the graphic design(how it looks) and then actually build the website in wordpress. Contestants will be judged based on their We want to aim for professional look, and also how modern it looks

*** we also might have the chance to work together in the future for both projects and upgrading this website, so it is a good opportunity to get to know each other.

We would need 5 pages:
1. landing page, scroll down page that tells customer what services we offer(full stack software development, website design, fintech, blockchain)
2. about us: place where we can post information about our team
3. services: tab that explain in detail about what we can offer ( there should be a sub page about fintech, web design, big data, blockchain and full stack development)
4. contact us: a contact page that

```html
<!DOCTYPE html>
<html lang="en">
<head>
<meta charset="utf-8">
<title>Fintech Consulting</title>
<link rel="stylesheet" href="https://fonts.googleapis.com/css2?family=Nunito+Sans:wght@400;600;700;800&display=swap">
<style>
  :root {
    --blue: #1e72bd;
    --gold: #e8b62a;
    --ink: #111418;
    --text: #555b63;
    --panel: #e5ecf4;
    --panel-deco: #d2d9e1;
    --white: #ffffff;
  }
  * { box-sizing: border-box; margin: 0; padding: 0; }
  html, body { width: 1200px; height: 2416px; overflow: hidden; }
  body { position: relative; background: var(--white); font-family: "Nunito Sans", sans-serif; color: var(--ink); }
  .abs { position: absolute; }

  .hero-bg { left: 0; top: 0; width: 1200px; height: 773px; }
  .site-nav { left: 0; top: 0; width: 1200px; height: 76px; background: rgba(242,244,246,0.92); }
  .logo { left: 119px; top: 16px; font-size: 31px; font-weight: 700; color: #3b3f44; }
  .nav-link { top: 28px; font-size: 16px; font-weight: 600; color: #2a2e33; }
  .nav-cta { left: 932px; top: 13px; width: 196px; height: 51px; background: var(--blue); color: var(--white); font-size: 17px; font-weight: 600; display: flex; align-items: center; justify-content: center; }

  .hero-title { left: 102px; top: 225px; font-size: 49px; font-weight: 800; line-height: 60px; color: var(--white); }
  .hero-cta { left: 101px; top: 400px; width: 258px; height: 57px; background: var(--gold); color: var(--white); font-size: 24px; font-weight: 700; display: flex; align-items: center; justify-content: center; gap: 22px; }
  .slider-dots { left: 543px; top: 560px; display: flex; gap: 11px; }
  .slider-dots span { width: 23px; height: 23px; border-radius: 50%; border: 2px solid var(--white); }
  .slider-dots .active { background: var(--blue); border-color: var(--blue); }
  .device { left: 734px; top: 156px; width: 259px; height: 515px; border-radius: 38px; background: linear-gradient(170deg, #eef2f6, #c3cfdc 60%, #dfe6ee); border: 6px solid #1c1d20; }
  .scroll-btn { left: 1036px; top: 540px; width: 68px; height: 68px; border-radius: 50%; background: var(--blue); border: 6px solid var(--white); display: flex; align-items: center; justify-content: center; }

  .section-title { font-size: 37px; font-weight: 800; color: var(--ink); }
  .body-copy { font-size: 16px; line-height: 33.3px; color: var(--text); }

  .divider { left: 584px; top: 813px; width: 1px; height: 274px; background: #dde2e7; }
  .tab-arrow { left: 584px; top: 899px; }
  .knowledge-card { left: 678px; top: 811px; width: 443px; height: 276px; background: var(--panel); overflow: hidden; }
  .knowledge-card h3 { position: absolute; left: 33px; top: 53px; font-size: 24px; font-weight: 700; }
  .btn-gold { background: var(--gold); color: var(--white); font-size: 19px; font-weight: 700; display: flex; align-items: center; justify-content: center; }
  .knowledge-card .btn-gold { position: absolute; left: 33px; top: 113px; width: 257px; height: 57px; }
  .brochure-art { position: absolute; right: 0; bottom: 0; width: 126px; height: 78px; background: var(--panel-deco); }

  .services-title { left: 0; width: 1200px; top: 1160px; text-align: center; }
  .services-rule { left: 477px; top: 1214px; width: 221px; height: 2px; background: var(--gold); }
  .services-rule::before { content: ""; position: absolute; left: 0; top: -3px; width: 96px; height: 6px; background: var(--gold); }
  .service-card { top: 1275px; width: 334px; height: 348px; background: var(--panel); border-radius: 3px; text-align: center; }
  .service-card h4 { margin-top: 27px; font-size: 23px; font-weight: 700; color: var(--blue); }
  .service-icon { width: 124px; height: 124px; border-radius: 50%; background: var(--white); margin: 28px auto 0; display: flex; align-items: center; justify-content: center; }
  .service-card p { margin: 22px auto 0; width: 278px; font-size: 15px; line-height: 23.3px; color: var(--text); }

  .team-photo { left: 0; top: 1700px; width: 600px; height: 320px; background: linear-gradient(120deg, #d9e3ee, #b9c9da 45%, #e7edf3); }
  .accent-bar { left: 600px; top: 1719px; width: 29px; height: 301px; background: var(--blue); }
  .advantage-fade { left: 0; top: 1780px; width: 1200px; height: 240px; background: linear-gradient(to bottom, rgba(30,114,189,0) 0%, rgba(30,114,189,0.35) 45%, var(--blue) 100%); }
  .feedback-band { left: 0; top: 2020px; width: 1200px; height: 396px; background: var(--blue); }
  .eyebrow { left: 636px; top: 1740px; font-size: 27px; font-weight: 700; color: var(--blue); }
  .advantage-title { left: 636px; top: 1780px; font-size: 32px; font-weight: 700; color: var(--ink); }
  .advantage-copy { left: 636px; top: 1834px; width: 400px; font-size: 15px; line-height: 30px; color: var(--text); opacity: 0.85; }
  .btn-ghost { left: 636px; top: 1977px; width: 252px; height: 54px; border: 1px solid rgba(255,255,255,0.25); color: rgba(255,255,255,0.35); font-size: 18px; font-weight: 600; display: flex; align-items: center; justify-content: center; }
  .feedback-title { left: 0; width: 1200px; top: 2184px; text-align: center; font-size: 38px; font-weight: 800; color: var(--white); }
</style>
</head>
<body>

<svg class="abs hero-bg" width="1200" height="773" viewBox="0 0 1200 773" role="img" aria-label="Blurred photo of a bright office with business people in the background">
  <defs>
    <linearGradient id="heroFill" x1="0" y1="0" x2="1" y2="1">
      <stop offset="0" stop-color="#aebcc8"/>
      <stop offset="0.5" stop-color="#c9d3dc"/>
      <stop offset="1" stop-color="#e6ebf0"/>
    </linearGradient>
  </defs>
  <polygon points="0,0 1200,0 1200,517 361,736 280,693 0,773" fill="url(#heroFill)"/>
</svg>

<header class="abs site-nav">
  <div class="abs logo">your logo</div>
  <a class="abs nav-link" style="left:387px">Home</a>
  <a class="abs nav-link" style="left:472px">What we do</a>
  <a class="abs nav-link" style="left:604px">Our work</a>
  <a class="abs nav-link" style="left:720px">Our Team</a>
  <a class="abs nav-link" style="left:833px">Contact</a>
  <a class="abs nav-cta">Get in toch</a>
</header>

<h1 class="abs hero-title">Offering the world leading<br>fintech services</h1>
<a class="abs hero-cta">Get in toch
  <svg width="12" height="16" viewBox="0 0 12 16"><polygon points="0,0 12,8 0,16" fill="#fff"/></svg>
</a>
<div class="abs slider-dots"><span></span><span class="active"></span><span></span></div>
<div class="abs device" role="img" aria-label="Smartphone showing a photo of two business people shaking hands"></div>
<div class="abs scroll-btn">
  <svg width="22" height="14" viewBox="0 0 22 14"><polyline points="2,2 11,11 20,2" fill="none" stroke="#fff" stroke-width="2.5"/></svg>
</div>

<section>
  <h2 class="abs section-title" style="left:110px;top:856px">What we Do</h2>
  <p class="abs body-copy" style="left:110px;top:918px;width:425px">At vero eos et accusamus et iusto odio dignissimos ducimus qui blanditiis praesentium voluptatum deleniti atque corrupti quos dolores et quas molestias excepturi sint occaecati cupiditate non provident</p>
  <div class="abs divider"></div>
  <svg class="abs tab-arrow" width="58" height="114" viewBox="0 0 58 114">
    <path d="M0,0 A57,57 0 0 1 0,114 Z" fill="var(--blue)"/>
    <polyline points="18,45 30,57 18,69" fill="none" stroke="#fff" stroke-width="2.5"/>
  </svg>
  <div class="abs knowledge-card">
    <h3>Get a free fintech knowledge</h3>
    <a class="btn-gold">Download Brochure</a>
    <div class="brochure-art" role="img" aria-label="Faint illustration of an open brochure"></div>
  </div>
</section>

<section>
  <h2 class="abs section-title services-title">Our services</h2>
  <div class="abs services-rule"></div>

  <article class="abs service-card" style="left:91px">
    <h4>Software Development</h4>
    <div class="service-icon"><svg width="70" height="30" viewBox="0 0 70 30"><polyline points="6,24 24,12 38,20 62,6" fill="none" stroke="#8a9097" stroke-width="3"/><circle cx="6" cy="24" r="4" fill="#8a9097"/><circle cx="62" cy="6" r="4" fill="#8a9097"/></svg></div>
    <p>On the other hand, we denounce with righteous indignation and dislike men who are so beguiled and demoralized by the charms.</p>
  </article>
  <article class="abs service-card" style="left:435px">
    <h4>Fintech technology</h4>
    <div class="service-icon"><svg width="96" height="40" viewBox="0 0 96 40"><polyline points="6,34 32,18 50,28 90,6" fill="none" stroke="#8a9097" stroke-width="3"/><circle cx="6" cy="34" r="4" fill="#8a9097"/><circle cx="90" cy="6" r="4" fill="#8a9097"/></svg></div>
    <p>On the other hand, we denounce with righteous indignation and dislike men who are so beguiled and demoralized by the charms.</p>
  </article>
  <article class="abs service-card" style="left:779px">
    <h4>Blockchain technology</h4>
    <div class="service-icon"><svg width="96" height="40" viewBox="0 0 96 40"><polyline points="6,34 32,18 50,28 90,6" fill="none" stroke="#8a9097" stroke-width="3"/><circle cx="6" cy="34" r="4" fill="#8a9097"/><circle cx="90" cy="6" r="4" fill="#8a9097"/></svg></div>
    <p>On the other hand, we denounce with righteous indignation and dislike men who are so beguiled and demoralized by the charms.</p>
  </article>
</section>

<section>
  <div class="abs team-photo" role="img" aria-label="Photo of a team of colleagues working together at a computer"></div>
  <div class="abs accent-bar"></div>
  <div class="abs advantage-fade"></div>
  <div class="abs feedback-band"></div>
  <div class="abs eyebrow">Our Advantage</div>
  <h2 class="abs advantage-title">The Investment Committee</h2>
  <p class="abs advantage-copy">At vero eos et accusamus et iusto odio dignissimos ducimus qui blanditiis praesentium voluptatum deleniti atque corrupti quos dolores et quas molestias excepturi sint occaecati cupiditate non provident</p>
  <a class="abs btn-ghost">Download Brochure</a>
  <h2 class="abs feedback-title">Feedback for more</h2>
</section>

</body>
</html>
```